Flyer
Zielgruppe
Ich möchte den bisher erstellten Flyer (habe ich hochgeladen) ein wnig 'umstylen', mit dem neuen Logo. Der 200 Euro Bonus sol als Geldschein dargestellt werden.

```html
<!DOCTYPE html>
<html lang="de">
<head>
<meta charset="utf-8">
<title>Kanzlei Forum – Flyer</title>
<link rel="stylesheet" href="https://fonts.googleapis.com/css2?family=Playfair+Display:wght@400;500&family=Poppins:wght@400;500&display=swap">
<style>
  :root {
    --backdrop: #ecebe8;
    --paper: #151413;
    --gold: #e6c07a;
    --gold-deep: #b98a3e;
    --cream: #f3e4c4;
    --ember: #e0762a;
  }
  * { margin: 0; padding: 0; box-sizing: border-box; }
  html, body { width: 1200px; height: 848px; overflow: hidden; background: var(--backdrop); }
  .canvas { position: relative; width: 1200px; height: 848px; }

  .flyer {
    position: absolute; top: 130px; width: 416px; height: 588px;
    background: var(--paper); overflow: hidden; color: var(--cream);
    box-shadow: 0 4px 10px rgba(0,0,0,.18);
  }
  .flyer--front { left: 162px; }
  .flyer--back  { left: 622px; }

  .glow-field { position: absolute; inset: 0; }
  .flyer--front .glow-field {
    background:
      radial-gradient(ellipse 120px 260px at 100% 10%, rgba(214,170,90,.28), transparent 70%),
      radial-gradient(ellipse 110px 90px at 0% 100%, rgba(214,170,90,.28), transparent 70%);
  }
  .flyer--back .glow-field {
    background:
      radial-gradient(ellipse 90px 260px at 0% 30%, rgba(214,170,90,.22), transparent 70%),
      radial-gradient(ellipse 130px 240px at 100% 85%, rgba(214,170,90,.3), transparent 70%);
  }

  .centered { position: absolute; left: 0; right: 0; text-align: center; }
  .serif { font-family: "Playfair Display", Georgia, serif; }
  .sans  { font-family: "Poppins", Arial, sans-serif; }

  .rule {
    position: absolute; height: 2px; left: 50%; transform: translateX(-50%);
    background: linear-gradient(90deg, transparent, rgba(224,118,42,.55) 25%, #ffd79a 50%, rgba(224,118,42,.55) 75%, transparent);
  }
  .rule::after {
    content: ""; position: absolute; left: 50%; top: -2px; width: 50px; height: 6px;
    transform: translateX(-50%); border-radius: 50%;
    background: radial-gradient(ellipse, rgba(255,220,150,.9), transparent 70%);
  }

  .brand-name { top: 60px; font-size: 27px; font-weight: 400; color: var(--gold); letter-spacing: .5px; }
  .brand-tagline { top: 100px; font-size: 12px; letter-spacing: 1.2px; color: var(--gold); }

  .bonus-frame {
    position: absolute; left: 106px; top: 160px; width: 205px; height: 133px;
    border: 3px solid var(--gold); border-radius: 5px;
    box-shadow: 0 0 14px 4px rgba(240,190,100,.55), inset 0 0 10px rgba(240,190,100,.35), 0 0 40px 16px rgba(200,140,60,.25);
  }
  .bonus-kicker { top: 178px; font-size: 8.6px; color: var(--cream); }
  .bonus-amount {
    top: 190px; font-size: 48px; font-weight: 500; color: var(--gold);
    font-family: "Poppins", Arial, sans-serif; letter-spacing: 1px;
  }
  .bonus-divider { position: absolute; left: 173px; top: 253px; width: 62px; height: 1px; background: var(--gold); }
  .bonus-label { top: 259px; font-size: 14px; color: var(--gold); letter-spacing: .5px; }

  .front-headline { top: 322px; font-size: 20px; line-height: 22px; color: var(--cream); }

  .benefits { position: absolute; list-style: none; }
  .benefits li { display: flex; align-items: center; color: var(--cream); }
  .benefits svg { flex: none; }
  .flyer--front .benefits { left: 87px; top: 393px; }
  .flyer--front .benefits li { height: 25px; font-size: 10px; gap: 8px; }
  .flyer--back .benefits { left: 80px; top: 290px; }
  .flyer--back .benefits li { height: 25.2px; font-size: 10.2px; gap: 8px; }

  .front-cta { top: 491px; font-size: 13px; color: var(--cream); }
  .front-cta b, .back-cta b { font-family: "Poppins", Arial, sans-serif; font-weight: 500; color: var(--gold); }
  .front-url { top: 515px; font-size: 8px; color: var(--cream); }
  .front-values { top: 550px; font-size: 11px; color: var(--cream); }

  .back-headline { top: 56px; font-size: 27px; line-height: 33px; color: var(--cream); }
  .back-intro { top: 169px; font-size: 9.8px; line-height: 17.6px; color: var(--cream); }
  .back-cta { top: 441px; font-size: 18px; color: var(--cream); }
  .back-url { top: 475px; font-size: 13px; color: var(--cream); }
</style>
</head>
<body>
<main class="canvas">

  <section class="flyer flyer--front">
    <div class="glow-field" role="img" aria-label="Goldener Funkenstaub an den Rändern"></div>

    <h1 class="centered serif brand-name">Kanzlei Forum</h1>
    <p class="centered sans brand-tagline">LAWYER NETWORK</p>
    <div class="rule" style="top:130px;width:310px"></div>

    <div class="bonus-frame"></div>
    <p class="centered serif bonus-kicker">Exklusiver Startvorteil für neue Mitglieder</p>
    <p class="centered bonus-amount">€200</p>
    <div class="bonus-divider"></div>
    <p class="centered serif bonus-label">BONUS</p>

    <h2 class="centered serif front-headline">Das exklusive Netzwerk<br>für ambitionierte Anwälte</h2>
    <div class="rule" style="top:380px;width:300px"></div>

    <ul class="benefits sans">
      <li><svg width="15" height="15" viewBox="0 0 16 16"><circle cx="8" cy="8" r="7" fill="none" stroke="#e6c07a" stroke-width="1.4"/><path d="M4.6 8.2l2.3 2.3 4.6-4.8" fill="none" stroke="#e6c07a" stroke-width="1.5" stroke-linecap="round" stroke-linejoin="round"/></svg>Hochwertiges Networking mit Top-Anwälten</li>
      <li><svg width="15" height="15" viewBox="0 0 16 16"><circle cx="8" cy="8" r="7" fill="none" stroke="#e6c07a" stroke-width="1.4"/><path d="M4.6 8.2l2.3 2.3 4.6-4.8" fill="none" stroke="#e6c07a" stroke-width="1.5" stroke-linecap="round" stroke-linejoin="round"/></svg>Zugang zu exklusiven Events</li>
      <li><svg width="15" height="15" viewBox="0 0 16 16"><circle cx="8" cy="8" r="7" fill="none" stroke="#e6c07a" stroke-width="1.4"/><path d="M4.6 8.2l2.3 2.3 4.6-4.8" fill="none" stroke="#e6c07a" stroke-width="1.5" stroke-linecap="round" stroke-linejoin="round"/></svg>Mehr Mandanten und neue Chancen</li>
    </ul>
    <div class="rule" style="top:475px;width:310px"></div>

    <p class="centered serif front-cta">Jetzt Mitglied werden und <b>€200</b> Bonus sichern</p>
    <p class="centered serif front-url">www.kanzlei-forum.de</p>
    <div class="rule" style="top:537px;width:210px"></div>
    <p class="centered serif front-values">Exklusiv &nbsp;•&nbsp; Diskret &nbsp;•&nbsp; Erfolgreich.</p>
  </section>

  <section class="flyer flyer--back">
    <div class="glow-field" role="img" aria-label="Goldener Funkenstaub an den Rändern"></div>

    <h2 class="centered serif back-headline">Ihr exklusives Netzwerk<br>für Anwälte</h2>
    <div class="rule" style="top:149px;width:310px"></div>

    <p class="centered sans back-intro">Kanzlei Forum verbindet ambitionierte Anwälte.<br>in einem hochwertigen und diskreten Netzwerk.<br>Ziel ist es, neue Kontakte zu schaffen, Synergien<br>zu nutzen und langfristigen Erfolg zu fördern.</p>
    <div class="rule" style="top:268px;width:300px"></div>

    <ul class="benefits sans">
      <li><svg width="15" height="15" viewBox="0 0 16 16"><circle cx="8" cy="8" r="7" fill="none" stroke="#e6c07a" stroke-width="1.4"/><path d="M4.6 8.2l2.3 2.3 4.6-4.8" fill="none" stroke="#e6c07a" stroke-width="1.5" stroke-linecap="round" stroke-linejoin="round"/></svg>Aufbau eines starken beruflichen Netzwerks</li>
      <li><svg width="15" height="15" viewBox="0 0 16 16"><circle cx="8" cy="8" r="7" fill="none" stroke="#e6c07a" stroke-width="1.4"/><path d="M4.6 8.2l2.3 2.3 4.6-4.8" fill="none" stroke="#e6c07a" stroke-width="1.5" stroke-linecap="round" stroke-linejoin="round"/></svg>Zugang zu ausgewählten Veranstaltungen</li>
      <li><svg width="15" height="15" viewBox="0 0 16 16"><circle cx="8" cy="8" r="7" fill="none" stroke="#e6c07a" stroke-width="1.4"/><path d="M4.6 8.2l2.3 2.3 4.6-4.8" fill="none" stroke="#e6c07a" stroke-width="1.5" stroke-linecap="round" stroke-linejoin="round"/></svg>Austausch auf höchstem fachlichen Niveau</li>
      <li><svg width="15" height="15" viewBox="0 0 16 16"><circle cx="8" cy="8" r="7" fill="none" stroke="#e6c07a" stroke-width="1.4"/><path d="M4.6 8.2l2.3 2.3 4.6-4.8" fill="none" stroke="#e6c07a" stroke-width="1.5" stroke-linecap="round" stroke-linejoin="round"/></svg>Neue Mandanten und Geschäftsmöglichkeiten</li>
    </ul>
    <div class="rule" style="top:412px;width:300px"></div>

    <p class="centered serif back-cta">Jetzt <b>€200</b> Bonus sichern:</p>
    <p class="centered serif back-url">www.kanzlei-forum.de</p>
    <div class="rule" style="top:515px;width:210px"></div>
  </section>

</main>
</body>
</html>
```